MTL Book cover redo

I wrote a book called Mending the Lantern over ten years ago. I have revised and update the book and need a new cover. It should reflect the original idea and correlate with volumes two and three that came out later. So it doesn't need to be completely different...but enough to make it easy to see that it is a new version.
My title needs to be updated as well as it should say Mending the Lantern 1 (to flow with volumes 2 and 3).

```html
<!DOCTYPE html>
<html lang="en">
<head>
<meta charset="utf-8">
<title>Mending the Lantern 1 – Cover</title>
<link rel="stylesheet" href="https://fonts.googleapis.com/css2?family=Black+Ops+One&family=Oswald:wght@400;600;700&display=swap">
<style>
  :root {
    --ink: #050505;
    --sky: #5cc6ec;
    --ember: #e8591c;
    --ember-hot: #f5a623;
    --paper: #ffffff;
    --deep-blue: #0a2a6e;
    --glow-blue: #2f7fe0;
  }
  * { margin: 0; padding: 0; box-sizing: border-box; }
  html, body {
    width: 848px; height: 1200px; overflow: hidden;
    background: var(--ink);
  }
  .cover {
    position: relative;
    width: 848px; height: 1200px;
    background: var(--ink);
    overflow: hidden;
  }
  .cover__blurb {
    position: absolute; top: 110px; left: 0; right: 0;
    text-align: center;
    font-family: "Oswald", sans-serif;
    font-weight: 600; font-style: italic;
    font-size: 40px; letter-spacing: 1px;
    color: var(--sky);
  }
  .cover__title {
    position: absolute; top: 170px; left: 0; right: 0;
    font-family: "Black Ops One", sans-serif;
    color: var(--sky);
    font-weight: 400;
    text-align: center;
    line-height: 1;
  }
  .title__main {
    display: block;
    font-size: 150px;
    letter-spacing: 2px;
  }
  .title__second {
    display: flex; align-items: flex-end; justify-content: center;
    margin-top: 6px;
  }
  .title__article {
    font-size: 60px; margin-right: 10px; margin-bottom: 16px;
  }
  .title__keyword {
    font-size: 118px; letter-spacing: -2px;
  }
  .title__volume {
    display: inline-block;
    width: 26px; height: 118px;
    margin-left: 12px; margin-bottom: -64px;
    background: linear-gradient(180deg, var(--ember-hot), var(--ember));
  }
  .cover__subtitle {
    position: absolute; top: 462px; left: 60px; width: 680px;
    text-align: right;
    font-family: "Oswald", sans-serif;
    font-weight: 600; font-size: 22px; letter-spacing: 1.2px;
    color: var(--sky);
  }
  .cover__art {
    position: absolute; top: 540px; left: 0; right: 0; height: 420px;
    background:
      radial-gradient(ellipse 48% 22% at 50% 52%, rgba(232,89,28,0.9), transparent 75%),
      radial-gradient(ellipse 75% 55% at 50% 52%, var(--glow-blue), var(--deep-blue) 60%, var(--ink) 100%);
  }
  .cover__author {
    position: absolute; top: 985px; left: 0; right: 0;
    text-align: center;
    font-family: "Black Ops One", sans-serif;
    font-size: 58px; letter-spacing: 1px;
    color: var(--paper);
  }
  .cover__foreword {
    position: absolute; top: 1065px; left: 0; right: 0;
    text-align: center;
    font-family: "Oswald", sans-serif;
    font-weight: 600; font-size: 32px; letter-spacing: 5px;
    color: var(--sky);
  }
</style>
</head>
<body>
  <main class="cover">
    <p class="cover__blurb">"A thrilling read!"</p>
    <h1 class="cover__title">
      <span class="title__main">Mending</span>
      <span class="title__second">
        <span class="title__article">the</span>
        <span class="title__keyword">LANTERN</span>
        <span class="title__volume" aria-label="1"></span>
      </span>
    </h1>
    <p class="cover__subtitle">Shadows, Signals and the Last Light Unveiled</p>
    <div class="cover__art" role="img" aria-label="Orange double helix glowing over swirling blue energy"></div>
    <p class="cover__author">Dr Samuel Reeve</p>
    <p class="cover__foreword">Foreword by Alan Mercer</p>
  </main>
</body>
</html>
```